Ironbark Shift Workforce

We are a underground coal mining labour hire company, needing a website that links into our online payroll (www.wagetrackly.com.au) and also need to have job applications page that is a preform with drop down menu,s with answers or check boxes. We would also need a 3 tier administration access for access to different files.
We are looking for an ongoing relationship with future app integration

Reason: There are a few more designs to come and I'm out at the mine for another week

Industry/Entity Type

Coal Mining

```html
<!DOCTYPE html>
<html lang="en">
<head>
<meta charset="utf-8">
<title>Ironbark Shift Workforce</title>
<link rel="stylesheet" href="https://fonts.googleapis.com/css2?family=Exo+2:wght@400;500;600;700;800&display=swap">
<style>
:root{
  --orange:#f07d1e;
  --black:#000;
  --nav:#1a1a1a;
  --ink:#1d1d1d;
  --white:#fff;
  --grey:#cfcfcf;
  --panel:rgba(24,24,24,.93);
}
*{box-sizing:border-box;margin:0;padding:0}
html,body{width:1200px;height:1029px;overflow:hidden;background:var(--white)}
body{position:relative;font-family:"Exo 2",sans-serif;color:var(--ink)}
.abs{position:absolute}

.topnav{left:0;top:0;width:1200px;height:63px;background:var(--nav);box-shadow:0 3px 6px rgba(0,0,0,.5);z-index:3}
.topnav a{position:absolute;top:25px;font-size:11px;font-weight:500;color:var(--white);text-decoration:none;letter-spacing:.2px}
.topnav a.is-active{color:var(--orange)}
.nav-icon{position:absolute;top:19px;width:26px;height:26px;background:#262626;display:flex;align-items:center;justify-content:center}
.nav-phone{position:absolute;left:919px;top:23px;display:flex;align-items:center;gap:6px;color:var(--orange);font-size:12px;font-weight:700}

.hero{left:0;top:63px;width:1200px;height:235px;background:radial-gradient(ellipse at 70% 40%,#4a4038 0%,#2a2622 45%,#161412 100%)}
.hero-mark{position:absolute;left:326px;top:76px;font-size:76px;font-weight:600;color:var(--white);letter-spacing:2px;line-height:1}
.hero-circle{position:absolute;left:500px;top:38px;width:150px;height:150px;border-radius:50%;background:var(--orange)}
.hero-name{position:absolute;left:683px;top:85px;font-size:28px;font-weight:800;color:var(--white);line-height:24px;text-transform:uppercase}

.values{left:0;top:298px;width:1200px;height:51px;background:var(--black)}
.values span{position:absolute;top:13px;font-size:22px;font-weight:800;color:var(--orange);letter-spacing:.5px}
.values-shadow{left:130px;top:349px;width:940px;height:40px;background:radial-gradient(ellipse at 50% 0%,rgba(0,0,0,.16) 0%,rgba(0,0,0,0) 70%)}

.welcome-title{left:183px;top:390px;width:560px;font-size:27px;font-weight:700;line-height:35px;text-transform:uppercase;color:#111}
.welcome-title em{font-style:normal;color:var(--orange)}
.welcome-text{left:186px;top:463px;width:550px;font-size:13.5px;line-height:17px;color:#111}
.btn-learn{left:184px;top:544px;width:172px;height:38px;border:1px solid var(--orange);color:var(--orange);font-size:13px;padding:11px 0 0 10px}

.quick-card{left:745px;width:270px;height:60px;border:1px solid #d8d8d8;border-radius:3px;background:var(--white);display:flex;align-items:center}
.quick-card.is-featured{border-color:var(--orange);box-shadow:3px 3px 4px rgba(0,0,0,.3);justify-content:center}
.brand-name{font-size:26px;font-weight:500;color:#2b2f8e;display:flex;align-items:center;gap:6px}
.brand-dot{width:22px;height:22px;background:#2b2f8e;border-radius:50%}
.quick-card .label{font-size:18px;font-weight:600;color:var(--grey);line-height:23px;margin-left:12px}
.quick-card svg{margin-left:22px}

.crew-band{left:0;top:622px;width:1200px;height:244px;background:linear-gradient(90deg,#5a4d40 0%,#3e3a34 30%,#6b5a48 55%,#4a443c 75%,#8c8378 100%)}
.info-panel{top:622px;height:244px;background:var(--panel);color:var(--white);padding:34px 0 0 19px}
.info-panel h2{font-size:19px;font-weight:500;color:var(--orange);margin-bottom:14px}
.info-panel p{font-size:12.5px;line-height:17px}
.info-panel .date{color:#9a9a9a;font-size:11.5px;margin-bottom:0}
.info-panel ul{list-style:none}
.info-panel li{font-size:12.5px;line-height:17px;padding-left:19px;position:relative;margin-bottom:7px}
.info-panel li::before{content:"";position:absolute;left:0;top:4px;width:9px;height:9px;background:var(--white)}
.btn-outline{display:inline-block;border:1px solid var(--white);font-size:11px;padding:5px 17px;color:var(--white)}

.footer-mark{left:532px;top:904px;display:flex;align-items:center;gap:8px}
.footer-circle{width:58px;height:58px;border-radius:50%;background:#111}
.footer-name{font-size:38px;font-weight:600;color:#111}
.copyright{left:0;top:968px;width:1200px;text-align:center;font-size:12.5px;color:#111}
</style>
</head>
<body>

<nav class="topnav abs">
  <a class="is-active" style="left:191px">HOME</a>
  <a style="left:259px">APPLICATION</a>
  <a style="left:364px">PAY PORTAL</a>
  <a style="left:461px">INFORMATION</a>
  <a style="left:569px">ABOUT US</a>
  <a style="left:654px">CONTACT</a>
  <a style="left:737px">MISSION</a>
  <span class="nav-icon" style="left:837px">
    <svg width="14" height="14" viewBox="0 0 14 14"><g fill="#f07d1e"><circle cx="11" cy="3" r="2"/><circle cx="3" cy="7" r="2"/><circle cx="11" cy="11" r="2"/></g><path d="M11 3L3 7l8 4" stroke="#f07d1e" stroke-width="1.3" fill="none"/></svg>
  </span>
  <span class="nav-icon" style="left:875px">
    <svg width="14" height="14" viewBox="0 0 14 14"><circle cx="5.5" cy="5.5" r="4" stroke="#f07d1e" stroke-width="1.6" fill="none"/><path d="M8.5 8.5l4 4" stroke="#f07d1e" stroke-width="2"/></svg>
  </span>
  <span class="nav-phone">
    <svg width="15" height="13" viewBox="0 0 15 13"><path d="M2 4c0-2 2-3 5.5-3S13 2 13 4l-2.5 1.5L9 4H6L4.5 5.5z" fill="#f07d1e"/><rect x="3" y="7" width="9" height="5" rx="1" fill="#f07d1e"/></svg>
    02 4000 7310
  </span>
</nav>

<section class="hero abs" role="img" aria-label="Mine rescue crew working underground in hard hats">
  <div class="hero-mark">ISW</div>
  <div class="hero-circle"></div>
  <div class="hero-name">Ironbark<br>Shift<br>Workforce</div>
</section>

<div class="values abs">
  <span style="left:357px">FLEXIBLE</span>
  <span style="left:527px">RESOURCEFUL</span>
  <span style="left:742px">RELIABLE</span>
</div>
<div class="values-shadow abs"></div>

<h1 class="welcome-title abs">Welcome to <em>Ironbark Shift Workforce</em></h1>
<p class="welcome-text abs">we are experienced in ground consolidation in underground coal mines,&nbsp; in short when they collapse or cave in we come in with chemical pumps and stabilise the ground or fill cavities which will then allow for the mining process to continue. We also do general mine labor as well.</p>
<div class="btn-learn abs">LEARN MORE
  <svg style="position:absolute;right:10px;top:13px" width="38" height="12" viewBox="0 0 38 12"><g fill="#f07d1e"><circle cx="2" cy="6" r="1.3"/><circle cx="7" cy="6" r="1.3"/><circle cx="12" cy="6" r="1.3"/><circle cx="17" cy="6" r="1.3"/><circle cx="22" cy="6" r="1.3"/><circle cx="27" cy="6" r="1.3"/><circle cx="31" cy="2" r="1.3"/><circle cx="31" cy="10" r="1.3"/><circle cx="35" cy="6" r="1.3"/></g></svg>
</div>

<div class="quick-card is-featured abs" style="top:388px">
  <span class="brand-name"><span class="brand-dot"></span>wagetrackly</span>
</div>
<div class="quick-card abs" style="top:455px">
  <svg width="34" height="26" viewBox="0 0 34 26"><rect x="1" y="1" width="26" height="18" rx="2" fill="none" stroke="#cfcfcf" stroke-width="2"/><path d="M6 7h10M6 11h14M6 15h8" stroke="#cfcfcf" stroke-width="2"/><circle cx="25" cy="17" r="5" fill="#fff" stroke="#cfcfcf" stroke-width="2"/><path d="M28.5 20.5l4 4" stroke="#cfcfcf" stroke-width="2.5"/></svg>
  <span class="label">Our Job Vacancies</span>
</div>
<div class="quick-card abs" style="top:522px">
  <svg width="34" height="30" viewBox="0 0 34 30"><circle cx="9" cy="12" r="4" fill="#cfcfcf"/><path d="M2 26c0-5 3-8 7-8s7 3 7 8z" fill="#cfcfcf"/><path d="M20 4h10M20 12h10M20 20h10M20 28h10M18 4v24" stroke="#cfcfcf" stroke-width="2.5"/></svg>
  <span class="label">Employee Benifit<br>Programs</span>
</div>

<div class="crew-band abs" role="img" aria-label="Mine workers in hard hats standing on a rocky site"></div>

<section class="info-panel abs" style="left:183px;width:257px">
  <h2>News</h2>
  <p class="date">12-12-2013</p>
  <p>we are experienced in ground consolidation in underground coal mines....</p>
  <span class="btn-outline" style="margin:17px 0 0 2px">ALL NEWS</span>
</section>

<section class="info-panel abs" style="left:470px;width:259px;padding-left:21px">
  <h2>Services</h2>
  <ul>
    <li>Roadheader Drivage / Tunnel Excavation</li>
    <li>Labour Hire</li>
    <li>Tunnel Excavation</li>
  </ul>
  <span class="btn-outline" style="margin-top:26px">SEE MORE</span>
</section>

<section class="info-panel abs" style="left:759px;width:258px;padding-left:22px">
  <h2>Engineering</h2>
  <p>Lorem ipsum dolor sit amet, consectetuer adipiscing elit, sed diam nonummy &nbsp;...</p>
  <p style="margin-top:5px">Design and engineering of specialised equipment and consumables</p>
  <span class="btn-outline" style="margin:15px 0 0 -2px">READ MORE</span>
</section>

<div class="footer-mark abs">
  <span class="footer-circle"></span>
  <span class="footer-name">ISW</span>
</div>
<p class="copyright abs">©2014&nbsp; Ironbark Shift Workforce – Underground Construction – Coal Mine Services</p>

</body>
</html>
```